Broschüre für eine Trainingsakademie
Zielgruppe
Ich möchte eine Broschüre zu meinem Unternehmen und meinen Angeboten schöner Design haben.
Ich bin Trainer/ Coach für moderne Personalstrategien insbesondere für die Personalgewinnung, Mitarbeiterbindung und -entwicklung. Zudem biete ich Trainings und Coachings für Mitarbeiter und Führungskräfte an. Zum Beispiel zu Themen wie gesunde Führung, Stressmanagement, Resilienz usw.
Meine Zielgruppe sind vor allem mittelständische Unternehmen oder junge aufstrebende StartUps, die ich beim Aufbau von Personalstrukturen unterstütze.
Aufgabenstellung
Mein Logo und die Farben sollen entsprechend berücksichtigt werden. Ein Entwurf für die Broschüre besteht bereits. Das ist allerdings nur meine Idee, als Laie. Ich hätte hier gern professionelle Ideen, so dass die Broschüre professionell und ansprechend wirkt.
Bilder habe ich eigentlich - diese finden sich auch auf meiner Homepage. Allerdings bin ich gerade auch beim Deckblatt offen. Auch für andere Gestaltungsvorschläge.

```html
<!DOCTYPE html>
<html lang="de">
<head>
<meta charset="utf-8">
<title>Hallmer Coaching – Broschüre</title>
<link rel="stylesheet" href="https://fonts.googleapis.com/css2?family=Arimo:wght@400;700&display=swap">
<style>
:root{
  --bg:#f2f2f4;
  --paper:#ffffff;
  --ink:#1f1f24;
  --muted:#6f6b80;
  --brand:#4f4a72;
  --accent:#5c5778;
  --band:#d9d6e3;
  --pagetab:#a9a5ba;
}
*{box-sizing:border-box;margin:0;padding:0}
html,body{width:1200px;height:600px;overflow:hidden}
body{background:var(--bg);font-family:"Arimo",Arial,sans-serif;color:var(--ink);position:relative}
.page{position:absolute;width:385px;height:272px;background:var(--paper);border:1px solid #3a3a44;overflow:hidden}
.page--2{left:39px;top:27px}
.page--3{left:405px;top:163px}
.page--4{left:774px;top:299px}
.chevrons{position:absolute;left:0;top:0;width:130px;height:130px}
.brand{position:absolute;left:278px;top:27px;width:80px;text-align:center;color:var(--brand);font-size:10.5px;letter-spacing:.6px;line-height:1}
.brand small{display:block;font-size:3.6px;letter-spacing:.5px;margin-top:1px;border-top:1px solid var(--brand);padding-top:1px}
.copy{position:absolute;font-size:6.6px;line-height:9.1px;text-align:justify}
.copy p+p{margin-top:9px}
.copy .num{font-size:10px}
.lists{position:absolute;left:206px;top:53px;width:150px;font-size:6.7px}
.lists h3{font-size:6.7px;font-weight:700;line-height:9px;display:flex;gap:6px}
.lists ol{list-style:lower-alpha;padding-left:24px;margin:5px 0 10px;font-size:5.7px;line-height:6.5px}
.rule-h{position:absolute;left:0;top:206px;height:1px;background:var(--accent)}
.rule-v{position:absolute;left:19px;top:194px;width:1px;height:56px;background:var(--accent)}
.headline{position:absolute;left:28px;top:211px;width:170px;font-size:7.6px;line-height:13px;color:#333;background:linear-gradient(90deg,rgba(217,214,227,.55),rgba(255,255,255,0))}
.headline b{font-size:10.8px;font-weight:400;color:var(--ink)}
.pagetab{position:absolute;left:343px;top:248px;width:14px;height:24px;background:var(--pagetab);color:#fff;font-size:9px;text-align:center;padding-top:4px}
.connector{position:absolute;left:0;top:0;width:385px;height:272px;pointer-events:none}
.figure{position:absolute;background:linear-gradient(180deg,#7a7495,#4f4a6c);border-radius:3px;opacity:.85}
.success{position:absolute;left:34px;top:163px;width:96px;height:29px;border-radius:14px;background:linear-gradient(90deg,#cfcbe0,#8f89ad,#cfcbe0)}
</style>
</head>
<body>

<section class="page page--2">
  <svg class="chevrons" viewBox="0 0 130 130" aria-hidden="true">
    <polygon points="0,0 14,0 60,46 0,106" fill="#e4e2ec"/>
    <polygon points="16,0 30,0 76,46 30,92 16,92 62,46" fill="#cfcbdc"/>
    <polygon points="36,0 50,0 70,20 63,27" fill="#dcd9e6"/>
  </svg>
  <div class="brand">HALLMER<small>COACHING</small></div>
  <div class="copy" style="left:28px;top:25px;width:154px">
    <p>Der Kampf um die besten Köpfe hat längst begonnen. Gute Bewerber können sich Ihre Arbeitgeber oft aussuchen. Viele Arbeitnehmer erhalten regelmäßig Anfragen von Headhuntern und Personaldienstleistern, die ihre Mitarbeiter abwerben wollen. Was können Sie tun?</p>
    <p>Zahlreiche Studien der letzten Jahre zeigen uns, was Mitarbeitern bei ihren Arbeitgebern hält und was ihnen in ihrem Job wichtig ist. Fangen Sie heute an, Ihre Mitarbeiter an Ihr Unternehmen zu binden! Was sich Arbeitnehmer von Ihren Arbeitgebern wünschen:</p>
  </div>
  <svg class="connector" aria-hidden="true">
    <g stroke="#555" stroke-width=".8" stroke-dasharray="1 1.5" fill="none">
      <path d="M190 58 H203 M190 58 V157 M190 134 H203 M195 178 H203"/>
    </g>
  </svg>
  <div class="lists">
    <h3><span>1.</span>Wohlgefühl bei der Arbeit</h3>
    <ol>
      <li>Wertschätzung der Arbeit</li>
      <li>Regelmäßiges Feedback/ eine gute Feedbackkultur</li>
      <li>Unterstützung bei Fragen und Problemen</li>
      <li>Gute Beziehung zu den Vorgesetzten und Kollegen</li>
      <li>Faire und attraktive Bezahlung</li>
    </ol>
    <h3><span>2.</span>Eine gesunde Work-Life-Balance</h3>
    <ol>
      <li>Flexible Arbeitszeiten/ Arbeitszeitmodelle</li>
      <li>Karriere in Teilzeit</li>
      <li>Stressreduktion</li>
    </ol>
    <h3><span>3.</span>Entwicklungsmöglichkeiten und Weiterbildungsangebote für Mitarbeiter</h3>
    <ol>
      <li>Regelmäßige Weiterbildungsangebote zur fachlichen und persönlichen Weiterentwicklung</li>
      <li>Anerkennung für geleistete Arbeit</li>
      <li>Attraktive Karrierepfade</li>
    </ol>
  </div>
  <div class="figure" role="img" aria-label="Silhouette einer gehenden Person" style="left:179px;top:161px;width:18px;height:45px"></div>
  <div class="rule-h" style="width:206px"></div>
  <div class="rule-v"></div>
  <p class="headline">Werden Sie zum <b>Magneten</b> für<br>Ihre Mitarbeiter und <b>Bewerber</b>!</p>
  <div class="pagetab">2</div>
</section>

<section class="page page--3">
  <svg class="chevrons" viewBox="0 0 130 130" aria-hidden="true">
    <polygon points="0,0 14,0 60,46 0,106" fill="#e4e2ec"/>
    <polygon points="16,0 30,0 76,46 30,92 16,92 62,46" fill="#cfcbdc"/>
  </svg>
  <div class="brand">HALLMER<small>COACHING</small></div>
  <div class="copy" style="left:29px;top:26px;width:150px">
    <p><span class="num">1.</span> Wenn das Unternehmen zum Mitarbeiter passt – und umgekehrt – dann klappt es auch mit dem Wohlfühl-Klima. Employer Branding ist daher für alle Arbeitgeber hochrelevant: Was macht uns aus und was bieten wir unseren Angestellten? Welche Mitarbeiter passen zu uns – und zueinander? Eine ehrliche Bestandsaufnahme und Kommunikation bildet dafür die Basis. Lernen Sie dann, wie Sie genau diese Passfähigkeit erkennen und dadurch die richtigen Mitarbeiter für Ihr Unternehmen einstellen!</p>
  </div>
  <div class="copy" style="left:206px;top:108px;width:144px">
    <p><span class="num">2.</span> Anerkennung für gute Arbeit. Das muss nicht unbedingt mit finanziellem Aufwand verbunden sein, auch wenn manche Arbeitgeber das befürchten: Untersuchungen zeigen immer wieder, dass schon ein ehrliches Lob Mitarbeiter ungleich stärker motiviert als es z. B. unpersönliche Motivations-Poster in der Kantine tun.</p>
  </div>
  <svg class="connector" aria-hidden="true">
    <g stroke="#555" stroke-width=".8" stroke-dasharray="1 1.5" fill="none">
      <path d="M196 67 H247 V101 M144 144 V179 H196"/>
    </g>
  </svg>
  <div class="success" role="img" aria-label="Grafik mit dem Schriftzug Success in Kreisen"></div>
  <div class="rule-h" style="width:205px"></div>
  <div class="rule-v"></div>
  <p class="headline">Was können Sie als <b>Arbeitgeber</b><br>nun konkret dafür <b>tun</b>?</p>
  <div class="figure" role="img" aria-label="Silhouette einer Person, die eine Stufe hinaufsteigt" style="left:323px;top:206px;width:31px;height:62px"></div>
  <div class="pagetab">3</div>
</section>

<section class="page page--4">
  <svg class="chevrons" viewBox="0 0 130 130" aria-hidden="true">
    <polygon points="0,0 14,0 60,46 0,106" fill="#e4e2ec"/>
    <polygon points="16,0 30,0 76,46 30,92 16,92 62,46" fill="#cfcbdc"/>
  </svg>
  <div class="brand">HALLMER<small>COACHING</small></div>
  <div class="copy" style="left:28px;top:26px;width:146px">
    <p><span class="num">3.</span> Feedback-Kultur schaffen und pflegen. Monatlich oder quartalsweise stattfindende Vier-Augen-Gespräche, wöchentliche Team-Kickoffs oder das 5-Minutengespräch zwischendurch helfen dranzubleiben.</p>
    <p><span class="num">4.</span> Als Arbeitgeber ansprechbar und nahbar bleiben. Das ist etwas, was täglich geübt werden kann und irgendwann zur Selbstständlichkeit wird. Hier haben übrigens besonders kleinere Unternehmen große Chancen!</p>
  </div>
  <div class="copy" style="left:206px;top:62px;width:146px">
    <p><span class="num">5.</span> Weiterbildungsmöglichkeiten bieten. Zeigen Sie, dass Ihnen die Entwicklung Ihrer Mitarbeiter wichtig ist. Davon haben nicht nur die Arbeitnehmer etwas, sondern auch das Unternehmen gewinnt!</p>
    <p><span class="num">6.</span> Entwicklungsperspektiven bieten! Viele Mitarbeiter können sich nur durch eine Führungskarriere in ihrem Unternehmen weiterentwickeln, die vielleicht aber gar nicht zu ihnen passt. Fachkarrieren können hier eine attraktive Alternative bieten, die ihre Mitarbeiter bei Ihnen hält.</p>
  </div>
  <svg class="connector" aria-hidden="true">
    <g stroke="#555" stroke-width=".8" stroke-dasharray="1 1.5" fill="none">
      <path d="M174 30 H223 V57 M144 136 V161 H195"/>
    </g>
  </svg>
  <div class="rule-h" style="width:205px"></div>
  <div class="rule-v"></div>
  <p class="headline">Was können Sie als <b>Arbeitgeber</b><br>nun konkret dafür <b>tun</b>?</p>
  <div class="figure" role="img" aria-label="Silhouette einer Person auf einer höheren Stufe" style="left:340px;top:193px;width:31px;height:79px"></div>
  <div class="pagetab">4</div>
</section>

</body>
</html>
```